TidalCover Mobile App needs a new skin

We need to add some sparkle to our mobile application. The app is already built with some of the functionality, screens and components (vanilla material design) and now it needs some styling and inspiration. The application simplifies insurance form capturing and communication to/from the broker. Further to that it has some value added services.

Industry/Entity Type

Insurance Broker

Font styles to use
Sans Serif

Requirements
Must have
• Modern, friendly styling and colors. Material design principles.
Nice to have
• Thinking of a themed background photo with the form elements in a more glassy / semi transparent style.
• Would like to use the same app for some customers as a white labeled version, then just change the themed background image, logo and select dark or light theme for them.

```html
<!DOCTYPE html>
<html lang="en">
<head>
<meta charset="utf-8">
<title>TidalCover – App Screens</title>
<link href="https://fonts.googleapis.com/css2?family=Montserrat:wght@400;500;600;700&display=swap" rel="stylesheet">
<style>
:root{
  --bg:#121618;
  --teal:#8dd2c6;
  --green:#86cf9c;
  --cyan:#14d2d8;
  --nav:#3b5c58;
  --nav-active:#8dd2c6;
  --remove:#d9838b;
  --field:#f3f4f4;
  --card:#f4f5f5;
  --ink:#2b2f31;
  --muted:#6e7478;
  --deep:#2f5551;
  --sign:#e07a7a;
}
*{box-sizing:border-box;margin:0;padding:0}
html,body{width:1200px;height:1200px;overflow:hidden;background:var(--bg)}
body{font-family:"Montserrat",sans-serif;color:var(--ink);position:relative}
.backdrop{position:absolute;inset:0;background:radial-gradient(ellipse at 50% 45%,#2a3337 0%,#171c1f 55%,#0e1113 100%)}
.screen{position:absolute;width:226px;height:402px;overflow:hidden;background:#fff}
.abs{position:absolute}
.photo{position:absolute;inset:0;background:linear-gradient(180deg,#3a4449 0%,#2b3235 40%,#1e2326 75%,#15191b 100%)}
.photo::after{content:"";position:absolute;left:20px;top:120px;width:110px;height:200px;border-radius:40px;background:radial-gradient(ellipse at 50% 50%,rgba(210,160,40,.35),rgba(0,0,0,0) 70%)}
.status{position:absolute;left:0;top:0;width:100%;height:13px;font-size:6.5px;display:flex;justify-content:space-between;align-items:center;padding:0 4px;color:#fff;z-index:3}
.brand{font-weight:500;color:#fff;letter-spacing:.5px}
.btn{position:absolute;display:flex;align-items:center;justify-content:center;color:#fff;font-weight:600;font-size:9px;letter-spacing:.3px}
.btn-cyan{background:var(--cyan)}
.btn-green{background:var(--green)}
.btn-remove{background:var(--remove)}
.appbar{position:absolute;left:0;top:0;width:100%;height:42px;background:var(--teal);color:#fff;font-size:8.5px;font-weight:600;display:flex;align-items:center;justify-content:center;padding-top:10px}
.appbar .bell{position:absolute;right:12px;top:22px;width:10px;height:10px}
.navbar{position:absolute;left:0;bottom:0;width:100%;height:32px;background:var(--nav);display:flex}
.navbar .tab{flex:1;display:flex;flex-direction:column;align-items:center;justify-content:center;color:#fff;font-size:6.5px;gap:1px}
.navbar .tab svg{width:14px;height:14px}
.navbar .tab.active{color:var(--nav-active)}
.card{position:absolute;left:10px;width:207px;background:var(--card)}
.card h4{font-size:8.5px;font-weight:600;margin:8px 10px 4px}
.card p{font-size:7px;color:var(--muted);margin:0 10px;line-height:1.4}
.msg{position:absolute;left:26px;width:182px;border-bottom:1px solid #e4e6e6;padding-bottom:6px}
.msg b{font-size:6.5px;font-weight:700;display:block}
.msg span{font-size:7.5px;color:var(--muted);display:block;margin-top:4px}
.msg i{position:absolute;right:0;top:0;font-style:normal;font-size:6px;color:#9aa}
.label{position:absolute;left:20px;font-size:8.5px;font-weight:600}
.field{position:absolute;left:10px;width:207px;background:var(--field);font-size:7.5px;color:var(--muted);padding:9px 18px;line-height:1.35}
.policy{position:absolute;left:12px;width:202px;background:var(--card);height:52px;font-size:9px}
.policy .k{position:absolute;left:17px;font-weight:600}
.policy .v{position:absolute;left:82px;white-space:nowrap;font-size:8.5px}
.line-field{position:absolute;left:16px;width:196px;border-bottom:1px solid rgba(255,255,255,.35);color:#fff;font-size:8.5px;padding-bottom:8px}
.pin{position:absolute;top:218px;width:34px;height:42px;border:1.5px solid var(--deep);display:flex;align-items:center;justify-content:center;font-size:20px;color:var(--deep)}
.pin.empty{border-color:#ddd}
.dim{position:absolute;inset:0;background:rgba(20,28,30,.82)}
</style>
</head>
<body>
<div class="backdrop" role="img" aria-label="Dark themed background photo of people holding umbrellas in the rain"></div>

<svg width="0" height="0" style="position:absolute">
  <symbol id="i-home" viewBox="0 0 16 16"><path d="M2 6 8 2l6 4M3 6h10M4 7v5M7 7v5M10 7v5M13 7v5M2 13h12" fill="none" stroke="currentColor" stroke-width="1.2"/></symbol>
  <symbol id="i-shield" viewBox="0 0 16 16"><path d="M8 1.5 13.5 3.5v4c0 3.5-2.5 6-5.5 7-3-1-5.5-3.5-5.5-7v-4z" fill="none" stroke="currentColor" stroke-width="1.2"/><path d="m5.5 8 2 2 3-3.5" fill="none" stroke="currentColor" stroke-width="1.2"/></symbol>
  <symbol id="i-claim" viewBox="0 0 16 16"><path d="M6 2h4v4l2 2v2H4V8l2-2zM3 12h10v2H3z" fill="none" stroke="currentColor" stroke-width="1.2"/></symbol>
  <symbol id="i-user" viewBox="0 0 16 16"><circle cx="8" cy="5" r="3" fill="none" stroke="currentColor" stroke-width="1.2"/><path d="M2.5 14.5c0-3 2.5-5 5.5-5s5.5 2 5.5 5z" fill="none" stroke="currentColor" stroke-width="1.2"/></symbol>
  <symbol id="i-bell" viewBox="0 0 12 12"><path d="M6 1.5c2 0 3.2 1.4 3.2 3.4V8l1 1.2H1.8L2.8 8V4.9C2.8 2.9 4 1.5 6 1.5zM5 10.2h2" fill="#fff" stroke="#fff" stroke-width=".8"/><circle cx="10" cy="2" r="1.6" fill="#e0575b"/></symbol>
</svg>

<!-- Splash -->
<section class="screen" style="left:18px;top:183px">
  <div class="photo" role="img" aria-label="Businessman under a black umbrella holding a yellow folder in the rain"></div>
  <div class="status"><span>●●●●● Carrier</span><span>9:23 AM</span><span>66% ▭</span></div>
  <div class="abs brand" style="left:0;width:100%;top:187px;text-align:center;font-size:23px">TidalCover</div>
  <div class="abs" style="left:0;bottom:0;width:130px;height:1px;background:#fff"></div>
</section>

<!-- Intro -->
<section class="screen" style="left:253px;top:183px">
  <div class="photo" role="img" aria-label="Businessman under a black umbrella holding a yellow folder in the rain"></div>
  <div class="status"><span>●●●●● Carrier</span><span>9:23 AM</span><span>66% ▭</span></div>
  <h1 class="abs" style="left:16px;top:68px;color:#fff;font-size:19px;font-weight:700;line-height:1.3">TIME TO MAKE<br>A LIFE DIFFERENCE</h1>
  <p class="abs" style="left:16px;top:124px;width:195px;color:#e8ecec;font-size:7.6px;line-height:1.38;text-align:justify">TidalCover provides Insurance Forms Processing services, making the whole data capture process painless for you, the payer, who receives forms in huge numbers in different formats. We ensure that the output data is in a database-ready format so that insurance carriers can verify a claim quickly and proceed with reimbursement.</p>
  <div class="abs" style="left:103px;top:281px;display:flex;gap:4px"><i style="width:4px;height:4px;border-radius:50%;background:var(--cyan)"></i><i style="width:4px;height:4px;border-radius:50%;background:#fff"></i><i style="width:4px;height:4px;border-radius:50%;background:#fff"></i></div>
  <div class="btn btn-cyan" style="left:60px;top:314px;width:106px;height:31px">LETS STARTED</div>
</section>

<!-- Get started -->
<section class="screen" style="left:487px;top:183px">
  <div class="photo" role="img" aria-label="Businessman under a black umbrella holding a yellow folder in the rain"></div>
  <div class="status"><span>●●●●● Carrier</span><span>9:23 AM</span><span>66% ▭</span></div>
  <div class="abs" style="left:0;width:100%;top:56px;text-align:center;color:#fff;font-size:13px">GET STARTED</div>
  <div class="abs" style="left:0;width:100%;top:79px;text-align:center;color:#e8ecec;font-size:7.5px">We can't wait to here what you think.</div>
  <div class="line-field" style="top:144px">First Name</div>
  <div class="line-field" style="top:186px">Last Name</div>
  <div class="line-field" style="top:228px">Mobile Number</div>
  <div class="btn btn-cyan" style="left:53px;top:285px;width:121px;height:32px;font-size:9.5px">CREATE ACCOUNT</div>
  <div class="abs" style="left:0;width:100%;top:343px;text-align:center;color:#fff;font-size:6.8px">Agree to the <span style="color:var(--cyan)">Terms and Condition.</span></div>
</section>

<!-- Verify -->
<section class="screen" style="left:722px;top:183px">
  <div class="abs" style="left:0;top:0;width:100%;height:129px;background:var(--teal)"></div>
  <div class="status"><span>●●●●● Carrier</span><span>9:23 AM</span><span>66% ▭</span></div>
  <svg class="abs" style="left:12px;top:25px" width="10" height="10" viewBox="0 0 10 10"><path d="M1 1l8 8M9 1 1 9" stroke="#fff" stroke-width="1.2"/></svg>
  <div class="abs brand" style="left:0;width:100%;top:55px;text-align:center;font-size:22px">TidalCover</div>
  <svg class="abs" style="left:96px;top:108px" width="34" height="34" viewBox="0 0 34 34"><path d="M2 13 17 2l15 11v19H2z" fill="#fff" stroke="var(--deep)" stroke-width="1.5"/><rect x="8" y="7" width="18" height="11" fill="var(--deep)"/><circle cx="12" cy="12.5" r="1" fill="#fff"/><circle cx="15.5" cy="12.5" r="1" fill="#fff"/><circle cx="19" cy="12.5" r="1" fill="#fff"/><circle cx="22.5" cy="12.5" r="1" fill="#fff"/><path d="M2 13l15 10 15-10M2 32l12-10M32 32 20 22" fill="none" stroke="var(--deep)" stroke-width="1.5"/></svg>
  <p class="abs" style="left:14px;width:198px;top:165px;text-align:center;font-size:8.6px;line-height:1.3">To verify your account, Please enter the PIN code we sent you via SMS.</p>
  <div class="pin" style="left:24px">4</div>
  <div class="pin" style="left:70px">6</div>
  <div class="pin" style="left:116px">7</div>
  <div class="pin empty" style="left:162px"></div>
  <svg class="abs" style="left:90px;top:296px" width="46" height="46" viewBox="0 0 46 46"><circle cx="23" cy="23" r="23" fill="var(--deep)"/><path d="M15 23h16M25 17l6 6-6 6" fill="none" stroke="#fff" stroke-width="1.5"/></svg>
  <div class="abs" style="left:0;width:100%;top:357px;text-align:center;font-size:9px;font-weight:600;color:var(--deep)">Resend Code</div>
</section>

<!-- Home -->
<section class="screen" style="left:956px;top:183px">
  <div class="status"><span>●●●●● Carrier</span><span>9:23 AM</span><span>66% ▭</span></div>
  <header class="appbar">HOME<svg class="bell"><use href="#i-bell"/></svg></header>
  <div class="card" style="top:54px;height:51px"><h4>Emergency</h4><p>Send S.O.S notification to your energency center and they will call back in seconds.</p></div>
  <div class="btn btn-green" style="left:10px;top:105px;width:207px;height:18px;font-size:8px">SEND S.O.S</div>
  <div class="card" style="top:134px;height:51px"><h4>Road Side Assistance</h4><p>24 Hour assistance for any breakdown or towing assistance.</p></div>
  <div class="btn btn-green" style="left:10px;top:185px;width:207px;height:18px;font-size:8px">REQUEST ASSISTANCE</div>
  <div class="abs" style="left:10px;top:219px;font-size:8.5px;font-weight:600">Message</div>
  <div class="msg" style="top:238px"><b>BROKER</b><span>Your claim was registered this morning.</span><i>01h</i></div>
  <div class="msg" style="top:278px"><b>INSURER</b><span>Your claim was paid into your account.</span><i>01h</i></div>
  <div class="msg" style="top:318px"><b>BROKER</b><span>Your claim was registered this morning.</span><i>01h</i></div>
  <div class="msg" style="top:358px;border:0"><b>INSURER</b><i>01h</i></div>
  <nav class="navbar">
    <div class="tab active"><svg><use href="#i-home"/></svg>Home</div>
    <div class="tab"><svg><use href="#i-shield"/></svg>Insure</div>
    <div class="tab"><svg><use href="#i-claim"/></svg>Claim</div>
    <div class="tab"><svg><use href="#i-user"/></svg>Profile</div>
  </nav>
</section>

<!-- Emergency modal -->
<section class="screen" style="left:134px;top:616px">
  <div class="status"><span>●●●●● Carrier</span><span>9:23 AM</span><span>66% ▭</span></div>
  <header class="appbar">HOME</header>
  <div class="card" style="top:54px;height:51px"><h4>Emergency</h4><p>Send S.O.S notification to your energency center and they will call back in seconds.</p></div>
  <div class="btn btn-green" style="left:10px;top:105px;width:207px;height:18px;font-size:8px">SEND S.O.S</div>
  <div class="msg" style="top:278px"><b>INSURER</b><span>Your claim was paid into your account.</span><i>01h</i></div>
  <div class="msg" style="top:318px"><b>BROKER</b><span>Your claim was registered this morning.</span><i>01h</i></div>
  <div class="msg" style="top:358px;border:0"><b>INSURER</b><i>01h</i></div>
  <nav class="navbar">
    <div class="tab"><svg><use href="#i-home"/></svg>Home</div>
    <div class="tab"><svg><use href="#i-shield"/></svg>Insure</div>
    <div class="tab"><svg><use href="#i-claim"/></svg>Claim</div>
    <div class="tab"><svg><use href="#i-user"/></svg>Profile</div>
  </nav>
  <div class="dim"></div>
  <div class="abs" style="left:17px;top:137px;width:194px;height:128px;background:#fff">
    <div style="margin:0 8px;padding:11px 0 8px;border-bottom:1px solid #e4e6e6;text-align:center;font-size:9.5px;font-weight:500">EMERGENCY</div>
    <div style="text-align:center;font-size:8px;color:var(--muted);margin-top:11px">Your emergency is being processed...</div>
    <div style="text-align:center;font-size:6.5px;color:var(--muted);margin-top:5px">Initial request received</div>
    <div class="btn btn-green" style="left:0;bottom:0;width:100%;height:24px;font-size:8.5px;font-weight:500">CLOSE</div>
  </div>
</section>

<!-- Profile -->
<section class="screen" style="left:369px;top:616px">
  <div class="abs" style="left:0;top:0;width:100%;height:132px;background:linear-gradient(180deg,#2b3235,#3a4449)" role="img" aria-label="Dark rainy umbrella themed header photo"></div>
  <div class="status"><span>●●●●● Carrier</span><span>9:23 AM</span><span>66% ▭</span></div>
  <div class="abs" style="left:0;width:100%;top:24px;text-align:center;color:#fff;font-size:8.5px;font-weight:600">MY PROFILE</div>
  <svg class="abs" style="right:12px;top:24px" width="10" height="10"><use href="#i-bell"/></svg>
  <div class="abs" style="left:0;width:100%;top:63px;text-align:center;color:#fff;font-size:11.5px;font-weight:600">RIAN KOTZE</div>
  <div class="abs" style="left:0;width:100%;top:79px;text-align:center;color:#fff;font-size:7px">rian.kotze@mailbox.com</div>
  <svg class="abs" style="left:176px;top:57px" width="10" height="10" viewBox="0 0 10 10"><path d="M1 9l1-3 5-5 2 2-5 5z" fill="none" stroke="#fff" stroke-width=".9"/></svg>
  <div class="btn btn-green" style="left:0;top:132px;width:100%;height:28px;font-size:9px">ADD POLICY</div>
  <div class="policy" style="top:173px"><span class="k" style="top:11px">Policy</span><span class="v" style="top:11px">ARU43575799</span><span class="k" style="top:27px">Broker</span><span class="v" style="top:27px">Tern Brokers Seabrook</span></div>
  <div class="btn btn-remove" style="left:12px;top:225px;width:202px;height:20px;font-size:8.5px">REMOVE</div>
  <div class="policy" style="top:251px"><span class="k" style="top:11px">Policy</span><span class="v" style="top:11px">ARU435345454</span><span class="k" style="top:27px">Broker</span><span class="v" style="top:27px">Tern Brokers Seabrook</span></div>
  <div class="btn btn-remove" style="left:12px;top:303px;width:202px;height:20px;font-size:8.5px">REMOVE</div>
  <div class="policy" style="top:329px"><span class="k" style="top:11px">Policy</span><span class="v" style="top:11px">ARU43577857</span><span class="k" style="top:27px">Broker</span><span class="v" style="top:27px">Tern Brokers Seabrook</span></div>
  <nav class="navbar">
    <div class="tab"><svg><use href="#i-home"/></svg>Home</div>
    <div class="tab"><svg><use href="#i-shield"/></svg>Insure</div>
    <div class="tab"><svg><use href="#i-claim"/></svg>Claim</div>
    <div class="tab active"><svg><use href="#i-user"/></svg>Profile</div>
  </nav>
</section>

<!-- Edit profile -->
<section class="screen" style="left:603px;top:616px">
  <div class="status"><span>●●●●● Carrier</span><span>9:23 AM</span><span>66% ▭</span></div>
  <header class="appbar">EDIT PROFILE</header>
  <svg class="abs" style="left:10px;top:24px" width="8" height="10" viewBox="0 0 8 10"><path d="M6 1 2 5l4 4" fill="none" stroke="#fff" stroke-width="1.2"/></svg>
  <div class="abs" style="right:10px;top:24px;color:#fff;font-size:8px;font-weight:500">Save</div>
  <div class="label" style="top:59px">First Name</div>
  <div class="field" style="top:73px;height:27px">RIAN</div>
  <div class="label" style="top:108px">Last Name</div>
  <div class="field" style="top:122px;height:27px">KOTZE</div>
  <div class="label" style="top:157px">Email</div>
  <div class="field" style="top:171px;height:27px">rian.kotze@mailbox.com</div>
  <div class="label" style="top:206px">Telephone</div>
  <div class="field" style="top:220px;height:27px">01987654320</div>
  <div class="label" style="top:255px">Address</div>
  <div class="field" style="top:269px;height:67px">12 Harbour Lane,<br>Seabrook<br>WC<br>7351</div>
  <div class="abs" style="right:17px;top:350px;font-size:7.5px;font-weight:500;color:var(--sign)">SIGN OUT</div>
  <nav class="navbar">
    <div class="tab"><svg><use href="#i-home"/></svg>Home</div>
    <div class="tab"><svg><use href="#i-shield"/></svg>Insure</div>
    <div class="tab"><svg><use href="#i-claim"/></svg>Claim</div>
    <div class="tab active"><svg><use href="#i-user"/></svg>Profile</div>
  </nav>
</section>

<!-- Claims -->
<section class="screen" style="left:835px;top:616px">
  <div class="status"><span>●●●●● Carrier</span><span>9:23 AM</span><span>66% ▭</span></div>
  <header class="appbar">CLAIMS<svg class="bell"><use href="#i-bell"/></svg></header>
  <div class="card" style="top:54px;height:63px"><h4>Please Note</h4><p>This Claim from should be used as soon as possibe after the mishap. Dates and locations are tracked automatically from your device where possible</p></div>
  <div class="btn btn-green" style="left:10px;top:117px;width:207px;height:18px;font-size:8px">DISMISS</div>
  <div class="label" style="top:154px">Policy Number</div>
  <div class="field" style="top:168px;height:27px">ARU39857458</div>
  <div class="label" style="top:203px">Date of loss</div>
  <div class="field" style="top:217px;height:27px">2016 – 08 – 16</div>
  <div class="label" style="top:252px">Time of loss</div>
  <div class="field" style="top:266px;height:27px">06 :09 pm</div>
  <div class="label" style="top:301px">Place of loss</div>
  <div class="field" style="top:315px;height:27px">45 Coral Ave, Bayview, CA, 90412</div>
  <svg class="abs" style="left:199px;top:323px" width="8" height="11" viewBox="0 0 8 11"><path d="M4 10.5S.8 6.6.8 4a3.2 3.2 0 0 1 6.4 0C7.2 6.6 4 10.5 4 10.5z" fill="#222"/><circle cx="4" cy="4" r="1.2" fill="#fff"/></svg>
  <nav class="navbar">
    <div class="tab"><svg><use href="#i-home"/></svg>Home</div>
    <div class="tab"><svg><use href="#i-shield"/></svg>Insure</div>
    <div class="tab"><svg><use href="#i-claim"/></svg>Claim</div>
    <div class="tab active"><svg><use href="#i-user"/></svg>Profile</div>
  </nav>
</section>
</body>
</html>
```